Web Developer Needs a Business Card Design

I need a personal business card design that represents me as a web developer for potential employers. I would like the background to be a dark color on the front for contrast with my logo and name. The back will have all my information along with a smaller version of the logo. I want something with a modern look and feel, not too conservative. This will be used for potential employers and freelance work.

Industry/Entity Type

Business

Contact Information for Business Card

Front should have my logo and name. The back should have all my personal information which would include: name: Tom Brevardi, phone: 570-614-9083, email: tombrevardi@mailwisp.com, website url: www.tombrevardi.com, logo, web developer.

Font styles to use
Sans Serif

Requirements
Must have
• Must include my logo. The color palette base color will be the logo color.

```html
<!DOCTYPE html>
<html lang="en">
<head>
<meta charset="utf-8">
<title>Tom Brevardi – Business Card</title>
<link href="https://fonts.googleapis.com/css2?family=Lato:wght@300;700&display=swap" rel="stylesheet">
<style>
  :root {
    --page-bg: #e4e5e7;
    --card-back: #00212c;
    --mint: #4de0b8;
    --text-light: #e6eef0;
    --photo-deep: #02212a;
    --photo-mid: #0a3a44;
    --photo-glow: #0b7a5c;
    --faint-ring: #01283a;
  }
  * { margin: 0; padding: 0; box-sizing: border-box; }
  html, body {
    width: 1200px; height: 1192px; overflow: hidden;
    background: var(--page-bg);
    font-family: "Lato", sans-serif;
  }
  .card {
    position: absolute;
    left: 262px;
    width: 676px;
    height: 397px;
    overflow: hidden;
  }
  .card-front { top: 144px; }
  .card-back { top: 621px; background: var(--card-back); }

  .front-photo {
    position: absolute; inset: 0;
    background:
      radial-gradient(circle at 83% 22%, var(--photo-glow) 0%, rgba(11,122,92,0) 38%),
      radial-gradient(circle at 40% 50%, var(--photo-mid) 0%, rgba(10,58,68,0) 55%),
      linear-gradient(135deg, var(--photo-deep) 0%, #0a3140 55%, #03202b 100%);
  }
  .front-brand {
    position: absolute; left: 50%; top: 50%;
    transform: translate(-50%, -50%);
    display: flex; flex-direction: column; align-items: center; gap: 14px;
  }
  .brand-circle {
    width: 70px; height: 70px; border-radius: 50%;
    border: 7px solid var(--mint);
  }
  .brand-name {
    color: var(--mint);
    font-weight: 700;
    font-size: 30px;
    letter-spacing: 0.5px;
  }

  .back-ring {
    position: absolute;
    left: 420px; top: 20px;
    width: 360px; height: 360px;
    border-radius: 50%;
    border: 26px solid var(--faint-ring);
  }
  .contact {
    position: absolute;
    right: 263px; top: 140px;
    text-align: right;
  }
  .contact-name {
    color: var(--mint);
    font-weight: 700;
    font-size: 17px;
    letter-spacing: -0.3px;
    margin-bottom: 30px;
  }
  .contact-line {
    color: var(--text-light);
    font-weight: 300;
    font-size: 17px;
    letter-spacing: 1px;
    line-height: 29px;
    position: relative;
  }
  .contact-line svg {
    position: absolute;
    right: -32px; top: 6px;
    width: 18px; height: 16px;
  }
</style>
</head>
<body>
  <section class="card card-front">
    <div class="front-photo" role="img" aria-label="Blurred photo of a person touching a glowing interface surrounded by communication and device icons"></div>
    <div class="front-brand">
      <div class="brand-circle"></div>
      <div class="brand-name">Tom Brevardi</div>
    </div>
  </section>

  <section class="card card-back">
    <div class="back-ring"></div>
    <div class="contact">
      <div class="contact-name">Tom Brevardi</div>
      <div class="contact-line">570-614-9083
        <svg viewBox="0 0 18 16" aria-hidden="true"><circle cx="9" cy="8" r="7" fill="none" stroke="#4de0b8" stroke-width="1.6"/><path d="M7 4.5 q3 3.5 0 7" fill="none" stroke="#4de0b8" stroke-width="2"/></svg>
      </div>
      <div class="contact-line">tombrevardi@mailwisp.com
        <svg viewBox="0 0 18 16" aria-hidden="true"><rect x="1" y="2" width="16" height="12" fill="#4de0b8"/><path d="M1 2 L9 9 L17 2 M1 14 L7 8 M17 14 L11 8" fill="none" stroke="#00212c" stroke-width="1.2"/></svg>
      </div>
      <div class="contact-line">www.tombrevardi.com
        <svg viewBox="0 0 18 16" aria-hidden="true"><circle cx="9" cy="8" r="7" fill="#4de0b8"/><path d="M2 8 H16 M9 1 V15 M3.5 4.5 H14.5 M3.5 11.5 H14.5" stroke="#00212c" stroke-width="1"/><ellipse cx="9" cy="8" rx="3.2" ry="7" fill="none" stroke="#00212c" stroke-width="1"/></svg>
      </div>
    </div>
  </section>
</body>
</html>
```